Business Card Design Project

We need a redesign of our business card.
We are a Consulting Property Developer called The Selwick Group
Updates

Thank you all for submissions. Just waiting on managment to decide.

Thank you,

Dorinda

Industry/Entity Type

Business

Requirements
Must have
• we like having the SG a focus in the back ground or on the side
Selwick is our company colour

the wording - property development
and - premium accommodation

our website www.selwickgroup.com.au

persons name
title

p: 1300 582914 f: 1300 582917 m: 0419358027
PO Box 2817, Brackenvale Qld 4215
e: admin@selwickgroup.com.au

```html
<!DOCTYPE html>
<html lang="en">
<head>
<meta charset="utf-8">
<title>The Selwick Group — Business Card</title>
<link rel="stylesheet" href="https://fonts.googleapis.com/css2?family=Arimo:ital,wght@0,400;1,400&family=Open+Sans:wght@400&display=swap">
<style>
  :root {
    --stage: #303132;
    --brand-red: #981c31;
    --card-grey: #5b5e60;
    --rule-grey: #7c8286;
    --text-light: #cfcfcf;
    --text-dark: #141414;
  }
  * { box-sizing: border-box; margin: 0; padding: 0; }
  html, body {
    width: 1200px;
    height: 534px;
    overflow: hidden;
    background: var(--stage);
  }
  .canvas {
    position: relative;
    width: 1200px;
    height: 534px;
  }
  .card {
    position: absolute;
    top: 119px;
    width: 517px;
    height: 295px;
    background: var(--card-grey);
    overflow: hidden;
  }
  .card--front { left: 62px; }
  .card--back { left: 620px; }

  .band {
    position: absolute;
    left: 0;
    width: 100%;
    height: 48px;
    background: var(--brand-red);
  }
  .band--top { top: 0; }
  .band--bottom { bottom: 0; }
  .band-edge {
    position: absolute;
    left: 0;
    width: 100%;
    height: 3px;
    background: var(--rule-grey);
  }
  .band-edge--top { top: 51px; }
  .band-edge--bottom { bottom: 51px; }

  /* Front */
  .brand-lockup {
    position: absolute;
    left: 22px;
    top: 106px;
    display: flex;
    align-items: center;
    gap: 12px;
  }
  .brand-mark {
    width: 14px;
    height: 14px;
    background: var(--brand-red);
  }
  .brand-name {
    font-family: "Open Sans", sans-serif;
    font-weight: 400;
    font-size: 38px;
    color: var(--text-light);
    letter-spacing: -0.5px;
    line-height: 1;
  }
  .brand-underline {
    position: absolute;
    left: 20px;
    top: 162px;
    width: 447px;
    height: 1px;
    background: var(--text-light);
  }
  .tagline {
    position: absolute;
    left: 0;
    top: 207px;
    width: 100%;
    text-align: center;
    font-family: "Arimo", sans-serif;
    font-style: italic;
    font-size: 12.5px;
    color: var(--text-dark);
  }

  /* Back */
  .back-brand {
    position: absolute;
    left: 18px;
    top: 118px;
    font-family: "Open Sans", sans-serif;
    font-weight: 400;
    font-size: 27px;
    color: var(--text-light);
    line-height: 1;
  }
  .back-rule {
    position: absolute;
    left: 18px;
    top: 179px;
    width: 240px;
    height: 1px;
    background: var(--text-light);
  }
  .divider {
    position: absolute;
    left: 257px;
    top: 85px;
    width: 1px;
    height: 125px;
    background: var(--text-light);
  }
  .contact {
    position: absolute;
    left: 268px;
    top: 86px;
    font-family: "Arimo", sans-serif;
    font-style: italic;
    font-size: 12px;
    line-height: 14px;
    color: var(--text-dark);
  }
  .contact__name { color: var(--brand-red); text-transform: uppercase; }
  .contact__title { margin-bottom: 5px; }
  .contact__address { margin-bottom: 9px; }
  .contact__line { line-height: 12.8px; }
  .contact__label {
    display: inline-block;
    width: 12px;
    color: var(--brand-red);
    font-size: 10px;
  }
</style>
</head>
<body>
<main class="canvas">
  <section class="card card--front" aria-label="Business card front">
    <div class="band band--top"></div>
    <div class="band-edge band-edge--top"></div>
    <div class="brand-lockup">
      <span class="brand-mark" aria-hidden="true"></span>
      <span class="brand-name">The Selwick Group</span>
    </div>
    <div class="brand-underline"></div>
    <p class="tagline">Property Development&nbsp; | &nbsp;Premium Accommodation</p>
    <div class="band-edge band-edge--bottom"></div>
    <div class="band band--bottom"></div>
  </section>

  <section class="card card--back" aria-label="Business card back">
    <div class="band band--top"></div>
    <div class="band-edge band-edge--top"></div>
    <p class="back-brand">The Selwick Group</p>
    <div class="back-rule"></div>
    <div class="divider"></div>
    <div class="contact">
      <p class="contact__name">John Doe</p>
      <p class="contact__title">Title</p>
      <p class="contact__address">PO Box 2817, Brackenvale Qld 4215</p>
      <p class="contact__line"><span class="contact__label">p:</span>1300 582914</p>
      <p class="contact__line"><span class="contact__label">f:</span>1300 582917</p>
      <p class="contact__line"><span class="contact__label">m:</span>0419358027</p>
      <p class="contact__line"><span class="contact__label">e:</span>admin@selwickgroup.com.au</p>
      <p class="contact__line"><span class="contact__label">w:</span>www.selwickgroup.com.au</p>
    </div>
    <div class="band-edge band-edge--bottom"></div>
    <div class="band band--bottom"></div>
  </section>
</main>
</body>
</html>
```